Tidal Hounds Dog Behaviour, Training and Natural Healthcare Business Card Design

I am an experienced and qualified dog behavioural trainer and natural animal healthcare consultant offering a range of services to help pet dog owners with the "whole dog".
COLOURS: A soft light blue in the background - can be fading out or split, red should also feature
LOGO: Dog, healing hands, silhouette, shadow
SERVICES: Behaviour Consults, Training, Complex Skills Coaching Walking Coaching, Diet & Nutrition, Environmental Enrichment, Lifestyle and Lifestage Adaptations, Massage, Natural Health Options
BY LINE: Happy Dogs, Happy Owners
VALUES: Promoting communication and connection between dogs and their owners.
FOCUS: Nutritional guidance and environmental adaptation are often needed to complete the package and increase the success rate of training and behaviour modification.

Target Market(s)

Everyone who has a dog who they wish to improve their relationship with

Industry/Entity Type

Communication

Contact Information for Business Card

Tidal Hounds, Rosalind Vukovic, 0417 286350, tidalhounds7@quellmail.net, www.tidalhounds7.net, Qualified Dog Behavioural Trainer and Natural Animal Healthcare Consultant

Font styles to use
Sans Serif
Script

Colors
85cae6
ec2027

Requirements
Must have
• A clear indication that it is a dog services business. A raised feature
Should not have
• Pawprints, cartoons

Files

```html
<!DOCTYPE html>
<html lang="en">
<head>
<meta charset="utf-8">
<title>Tidal Hounds – Business Card</title>
<link href="https://fonts.googleapis.com/css2?family=Arimo:wght@400;700&display=swap" rel="stylesheet">
<style>
  :root {
    --page-bg: #ebe8e3;
    --blue-light: #1fa8e6;
    --blue-deep: #1d3f9e;
    --red-bright: #ec2027;
    --red-deep: #7d1116;
    --cream: #f3ecd2;
    --cream-ring: #c51d24;
    --text-light: #ffffff;
    --text-dark: #1a1a1a;
  }
  html, body {
    margin: 0;
    padding: 0;
    width: 1200px;
    height: 1000px;
    overflow: hidden;
    background: var(--page-bg);
    font-family: "Arimo", Arial, sans-serif;
  }
  .canvas {
    position: relative;
    width: 1200px;
    height: 1000px;
  }
  .card {
    position: absolute;
    left: 210px;
    width: 780px;
    height: 446px;
    border-radius: 22px;
    overflow: hidden;
    box-shadow: 0 6px 18px rgba(0,0,0,0.18);
  }
  .card--front { top: 36px; }
  .card--back { top: 518px; }
  .card svg { display: block; }
  .brand-name { font-weight: 700; letter-spacing: 3px; }
  .tagline { letter-spacing: 1px; }
</style>
</head>
<body>
<main class="canvas">

  <section class="card card--front" aria-label="Card front">
    <svg width="780" height="446" viewBox="0 0 780 446" xmlns="http://www.w3.org/2000/svg">
      <defs>
        <linearGradient id="frontBlue" x1="0" y1="0" x2="0" y2="1">
          <stop offset="0" stop-color="var(--blue-light)"/>
          <stop offset="1" stop-color="var(--blue-deep)"/>
        </linearGradient>
        <linearGradient id="frontRed" x1="0" y1="0" x2="1" y2="0">
          <stop offset="0" stop-color="var(--red-deep)"/>
          <stop offset="0.55" stop-color="var(--red-bright)"/>
          <stop offset="1" stop-color="var(--red-deep)"/>
        </linearGradient>
      </defs>
      <rect class="front-bg" width="780" height="446" fill="url(#frontBlue)"/>
      <path class="front-swoop" d="M0,430 C260,412 560,345 780,282 L780,446 L0,446 Z" fill="url(#frontRed)"/>
      <path class="front-swoop-line" d="M0,430 C260,412 560,345 780,282" fill="none" stroke="var(--cream)" stroke-width="4"/>

      <circle class="brand-mark" cx="390" cy="108" r="68" fill="var(--cream)" stroke="var(--cream-ring)" stroke-width="12"/>
      <text class="brand-name" x="390" y="234" text-anchor="middle" font-size="56" fill="var(--text-light)">TIDAL HOUNDS</text>
      <text class="tagline" x="390" y="276" text-anchor="middle" font-size="27" fill="var(--text-light)">HAPPY DOGS, HAPPY OWNERS</text>

      <text class="website" x="470" y="408" text-anchor="middle" font-size="19" fill="var(--text-light)">www.tidalhounds7.net</text>
    </svg>
  </section>

  <section class="card card--back" aria-label="Card back">
    <svg width="780" height="446" viewBox="0 0 780 446" xmlns="http://www.w3.org/2000/svg">
      <defs>
        <linearGradient id="backBlue" x1="0" y1="0" x2="0" y2="1">
          <stop offset="0" stop-color="var(--blue-light)"/>
          <stop offset="1" stop-color="#1873c4"/>
        </linearGradient>
        <radialGradient id="backRed" cx="0.55" cy="0.35" r="0.7">
          <stop offset="0" stop-color="var(--red-bright)"/>
          <stop offset="1" stop-color="var(--red-deep)"/>
        </radialGradient>
      </defs>
      <rect class="back-blue" width="780" height="238" fill="url(#backBlue)"/>
      <rect class="values-band" y="238" width="780" height="34" fill="var(--cream)"/>
      <rect class="back-red" y="272" width="780" height="174" fill="url(#backRed)"/>

      <circle class="brand-mark" cx="150" cy="98" r="62" fill="var(--cream)" stroke="var(--cream-ring)" stroke-width="11"/>
      <text class="brand-name" x="150" y="204" text-anchor="middle" font-size="20" fill="var(--text-light)">TIDAL HOUNDS</text>

      <line class="divider" x1="300" y1="40" x2="300" y2="214" stroke="var(--text-light)" stroke-width="1.5" opacity="0.8"/>

      <g class="services" fill="var(--text-light)">
        <text x="326" y="64" font-size="23">SERVICES</text>
        <text x="326" y="100" font-size="18.5">Behaviour Consults, Training,</text>
        <text x="326" y="128" font-size="18.5">Complex Skills and Walking Coaching,</text>
        <text x="326" y="156" font-size="18.5">Diet &amp; Nutrition, Massage,</text>
        <text x="326" y="184" font-size="18.5">Natural Healthcare Options</text>
      </g>

      <text class="values-line" x="390" y="262" text-anchor="middle" font-size="19" fill="var(--text-dark)">Promoting communication and connection between dogs and their families</text>

      <g class="person" fill="var(--text-light)" text-anchor="middle">
        <text x="240" y="324" font-size="32">Rosalind Vukovic</text>
        <text x="240" y="356" font-size="18.5">Qualified Dog Behavioural Trainer</text>
        <text x="240" y="382" font-size="18.5">and Natural Animal Healthcare Consultant</text>
      </g>

      <line class="divider" x1="455" y1="296" x2="455" y2="392" stroke="var(--text-light)" stroke-width="1.5" opacity="0.8"/>

      <g class="contact contact--phone">
        <circle cx="482" cy="320" r="12" fill="var(--text-light)"/>
        <rect x="477" y="312" width="10" height="16" rx="2" fill="none" stroke="var(--red-deep)" stroke-width="2"/>
        <text x="504" y="328" font-size="21" fill="var(--text-light)">0417 286350</text>
      </g>
      <g class="contact contact--email">
        <circle cx="482" cy="360" r="12" fill="var(--text-light)"/>
        <rect x="475" y="354" width="14" height="11" fill="none" stroke="var(--red-deep)" stroke-width="1.8"/>
        <path d="M475,354 L482,361 L489,354" fill="none" stroke="var(--red-deep)" stroke-width="1.8"/>
        <text x="504" y="367" font-size="18.5" fill="var(--text-light)">tidalhounds7@quellmail.net</text>
      </g>
    </svg>
  </section>

</main>
</body>
</html>
```